Buch-/eBook-Cover für ein Rivora PLT Taschenbuch
Zielgruppe
Wald & Stein Verlag ist ein moderner Verlag für islamische Bücher über innere Heilung, Herzruhe und persönliche Entwicklung im Licht des Qurans und der Sunnah. Der Verlag verbindet spirituelle Tiefe mit emotionalen Alltagsthemen wie Overthinking, Angst, Sabr, Tawakkul, Selbstheilung und innerem Frieden.
Aufgabenstellung
Wir benötigen ein modernes! Cover für ein Rivora PLT Taschenbuch in deutscher Sprache.
Titel: Oh je, meine Tage laufen davon weiter
Untertitel: Wie du durch kleine Schritte Halt gewinnst - selbst wenn dein Alltag dich stark fordert
Autorenname: Lotte Brenk
Verlagsname: Wald & Stein Verlag
Nische: Islam + Overthinking
Zielgruppe: Islamische Frauen
Vermarktung: Über Flixo
Es soll ein emotional ansprechendes Cover erstellt werden im modernen Design in deutscher Sprache für die Zielgruppe islamische Frauen.
Cover für Rivora PLT
Maße:
15,24 x 22,86 cm
6 x 9 Zoll
Vorder und Rückseite
E-Book E-Book"
Das Design darf nicht zu überladen sein.

```html
<!DOCTYPE html>
<html lang="de">
<head>
<meta charset="utf-8">
<title>Oh je – Meine Tage Laufen Davon Weiter</title>
<link rel="stylesheet" href="https://fonts.googleapis.com/css2?family=Open+Sans:wght@400;600;700&family=Sansita+Swashed:wght@400;500&display=swap">
<style>
  :root {
    --page-bg: #e6e6e6;
    --sky-top: #1b2230;
    --sky-blue: #3e4a66;
    --sky-violet: #5c4a68;
    --sky-rose: #a8606a;
    --sky-glow: #d9735e;
    --sea-dark: #2a2226;
    --ground: #120f12;
    --text-light: #ffffff;
    --text-shadow: rgba(0, 0, 0, 0.85);
  }
  * { margin: 0; padding: 0; box-sizing: border-box; }
  html, body {
    width: 966px;
    height: 1200px;
    overflow: hidden;
    background: var(--page-bg);
  }
  .cover {
    position: absolute;
    left: 123px;
    top: 59px;
    width: 720px;
    height: 1080px;
    overflow: hidden;
    color: var(--text-light);
    text-align: center;
    font-family: "Open Sans", sans-serif;
  }
  .cover-photo {
    position: absolute;
    inset: 0;
    background:
      radial-gradient(ellipse 70% 18% at 75% 58%, rgba(217, 115, 94, 0.65), transparent 70%),
      linear-gradient(to bottom,
        var(--sky-top) 0%,
        var(--sky-blue) 22%,
        var(--sky-violet) 40%,
        var(--sky-rose) 55%,
        var(--sky-glow) 66%,
        var(--sky-violet) 74%,
        var(--sea-dark) 82%,
        var(--ground) 100%);
  }
  .author {
    position: absolute;
    top: 28px;
    left: 0;
    right: 0;
    font-family: "Sansita Swashed", cursive;
    font-size: 26px;
    text-shadow: 0 1px 3px var(--text-shadow);
  }
  .title {
    position: absolute;
    top: 318px;
    left: 0;
    right: 0;
    font-family: "Sansita Swashed", cursive;
    font-weight: 400;
    font-size: 132px;
    line-height: 1;
    -webkit-text-stroke: 2px #1a1a1a;
    text-shadow: 3px 4px 0 #1a1a1a, 0 4px 10px var(--text-shadow);
  }
  .subtitle {
    position: absolute;
    top: 490px;
    left: 0;
    right: 0;
    font-size: 33px;
    font-weight: 400;
    text-shadow: 1px 2px 2px var(--text-shadow), 0 0 3px var(--text-shadow);
  }
  .tagline {
    position: absolute;
    top: 583px;
    left: 0;
    right: 0;
    font-size: 20px;
    line-height: 25px;
    text-shadow: 1px 1px 2px var(--text-shadow), 0 0 3px var(--text-shadow);
  }
  .publisher {
    position: absolute;
    top: 1012px;
    left: 0;
    right: 0;
    font-size: 18px;
    line-height: 26px;
  }
  .publisher-name {
    display: block;
    font-weight: 700;
    font-size: 21px;
  }
</style>
</head>
<body>
  <main class="cover">
    <div class="cover-photo" role="img" aria-label="Foto: Silhouette einer Frau mit Kopftuch, die am Meeresufer bei Sonnenuntergang betet, unter kahlen Ästen"></div>
    <p class="author">Lotte Brenk</p>
    <h1 class="title">Oh je</h1>
    <h2 class="subtitle">Meine Tage Laufen Davon Weiter</h2>
    <p class="tagline">Wie du durch kleine Schritte Halt gewinnst -<br>selbst wenn dein Alltag dich stark fordert</p>
    <p class="publisher">Verlagsname:<span class="publisher-name">Wald &amp; Stein Verlag</span></p>
  </main>
</body>
</html>
```